Luxury skin care/beauty salon needs a fresh wordpress website makeover

Today we have a wordpress site that has served us well, and we want to stay with wordpress, but we need a new up to date fresh look, with an inviting and enticing front, and look that just draws people in to book an appoint for luxury beauty treatment.

The salon consists of beautisian/skin specialint, a cosmetical nurse, and a doctor, - so top notch expertice within skin care and beauty treatment.

- The site should be integrated with Postwren (which we currently do not use.

- The site should further be able to "show prices for treatments" in a manner that matches the new website in style and layout, - we do show prices today via ex. the booking module from a vendor, but its done via iFrame

- booking needs to be very easy and intuitive, and the site needs to be response, since 75% of our customers use Ipad or mobile phone while booking

- the colours of the logo and style for the company today is primarily gold and black, and the shop is kept in a minimalistic style

- we have fresh newly made professional pictures made, and we can also later supply a video for ex. a landing page

- we have a license for Framewick if that can be utilized

- we need to be able to translate all elements into minimum Norwegian

- we use QL and Snapvale today to promote our services, if that can be incorporated, that would be a promotion plus

today we have the following pages
- main page
- a treatment page, where treatments are in more detail explained, this also doubles as pricelist ... we might look to discard this, since its manually updated and is not the master ... the master is the booking system, which also contains princes
- a portfolio page, seperated into types of treatments, this page also has one element of Snapvale which is one of the prime social media channals.
- a team member page, that presents the staff
- a contact us page
- a booking page ( that uses the national available booking system that we want to keep, but present in a different manner if possible) .. including gift card

we are not nessesarily looking to keep all pages, if the new design comes up with a more proffesional and smoother look, so this is debatable, so i have left the "How many web pages do you need designed?" to 4 pages .. again debatable

The final design should communicate luxury and professional skincare and beauty treatments, and easy booking.

Target Market(s)

Women or men that want to book a beauty or skin care treatment

Industry/Entity Type

Beauty and skin care salon

Coding

Coded - Design and coding required

Number of Pages Required

4 page

Colors

Designer to choose colors to be used in the design.

Requirements
Must have
• booking system, a connection to postwren, ability to change wording/language (Norwegian)
Nice to have
• video background, if it compliments the design
Should not have
• a new booking platform, we want to stick with the one we have

```html
<!DOCTYPE html>
<html lang="en">
<head>
<meta charset="utf-8">
<title>Lumera – Team</title>
<link href="https://fonts.googleapis.com/css2?family=Montserrat:wght@400;500;700&family=Lato:wght@400;700&family=Cormorant+Garamond:wght@500&display=swap" rel="stylesheet">
<style>
:root{
  --gold:#e2c572;
  --dark:#232323;
  --darker:#1c1c1c;
  --line:#3b3b3b;
  --line-soft:#4a4a4a;
  --white:#ffffff;
  --field:#444444;
  --ink:#2a2a2a;
}
*{margin:0;padding:0;box-sizing:border-box}
html,body{width:784px;height:1200px;overflow:hidden}
body{background:var(--gold);font-family:"Lato",sans-serif;color:var(--white);position:relative}
.page{position:absolute;left:17px;top:18px;width:750px;height:1164px;background:var(--dark)}
.abs{position:absolute}

/* header */
.header-photo{position:absolute;left:0;top:0;width:750px;height:108px;
  background:linear-gradient(90deg,#242321 0%,#2b2a27 45%,#4a4843 75%,#6a6761 100%)}
.topbar{font-size:8px;letter-spacing:-.1px}
.topbar-rule{left:34px;top:27px;width:681px;height:1px;background:rgba(255,255,255,.15)}
.mini-social{width:7px;height:7px;background:var(--white);border-radius:1px}
.logo{left:38px;top:54px;font-family:"Cormorant Garamond",serif;font-weight:500;font-size:22px;color:var(--gold);letter-spacing:1px}
.nav a{position:absolute;top:61px;font-size:9px;color:var(--white);text-decoration:none;text-transform:uppercase}
.nav .active::after{content:"";position:absolute;left:0;right:0;top:13px;height:2px;background:var(--gold)}

/* section title */
.section-title{left:0;width:750px;top:154px;text-align:center;font-family:"Montserrat",sans-serif;font-weight:400;font-size:13.5px;letter-spacing:3px}
.section-title-rule{left:366px;top:179px;width:18px;height:1px;background:var(--white)}

/* team cards */
.team-card{position:absolute;width:331px;height:223px;border:1px solid var(--line)}
.team-photo{position:absolute;left:6px;top:6px;width:317px;height:211px}
.team-photo::after{content:"";position:absolute;inset:0;background:linear-gradient(180deg,transparent 60%,rgba(0,0,0,.45))}
.team-name{position:absolute;left:0;width:329px;top:184px;text-align:center;font-family:"Montserrat",sans-serif;font-size:11px;letter-spacing:2.6px;z-index:2}
.learn-more{position:absolute;left:125px;top:210px;width:78px;height:24px;border:1px solid var(--gold);background:var(--dark);font-family:"Montserrat",sans-serif;font-size:6.5px;line-height:22px;text-align:center;z-index:2}

.to-top{position:absolute;width:30px;height:21px;background:var(--darker);display:flex;align-items:center;justify-content:center}

/* CTA */
.cta-rule{left:0;top:822px;width:750px;height:1px;background:var(--line)}
.cta{left:34px;top:772px;width:681px;height:67px;background:var(--gold);color:var(--ink)}
.cta-text{left:17px;top:28px;font-size:9.5px;text-transform:uppercase}
.cta-btn{left:540px;top:18px;width:118px;height:27px;background:var(--darker);color:var(--white);font-family:"Montserrat",sans-serif;font-size:6.5px;line-height:27px;text-align:center}

/* footer */
.widget-title{position:absolute;top:880px;width:157px;height:29px;border:1px solid var(--line-soft);font-family:"Montserrat",sans-serif;font-size:7.8px;line-height:27px;text-align:center}
.widget-title::after{content:"";position:absolute;left:74px;bottom:-4px;width:6px;height:6px;background:var(--dark);border-right:1px solid var(--line-soft);border-bottom:1px solid var(--line-soft);transform:rotate(45deg)}
.body-copy{font-size:9.4px;line-height:14px;color:var(--white)}
.hours-row{position:absolute;left:34px;width:158px;height:26px;border-bottom:1px solid var(--line-soft);font-size:9.5px;line-height:20px}
.hours-row b{display:inline-block;width:62px}
.article{position:absolute;left:209px;width:157px}
.article h3{font-family:"Montserrat",sans-serif;font-weight:700;font-size:9.8px;line-height:11.5px}
.article time{display:block;font-size:6.5px;margin-top:3px;text-transform:uppercase}
.article-rule{position:absolute;left:209px;width:157px;height:1px;background:var(--line-soft)}
.social-box{position:absolute;top:1019px;width:24px;height:24px;background:var(--gold);display:flex;align-items:center;justify-content:center}
.social-box span{width:9px;height:9px;border:1.5px solid var(--ink);border-radius:1px}
.email-field{left:558px;top:920px;width:157px;height:29px;background:var(--field);font-size:8px;color:#a0a0a0;padding:10px 9px}
.subscribe{left:558px;top:958px;width:157px;height:24px;border:1px solid var(--gold);font-family:"Montserrat",sans-serif;font-size:6.5px;line-height:22px;text-align:center}

.bottom-rule{left:0;top:1129px;width:750px;height:1px;background:var(--line)}
.copyright{left:0;width:750px;top:1140px;text-align:center;font-size:7.5px;font-weight:700;letter-spacing:-.2px}
</style>
</head>
<body>
<div class="page">
  <header>
    <div class="header-photo" role="img" aria-label="Header photograph: dark sand backdrop with a white orchid"></div>
    <div class="abs topbar" style="left:34px;top:9px">+00 222 3333 444 (08:00 - 19:00)</div>
    <div class="abs mini-social" style="left:170px;top:11px"></div>
    <div class="abs mini-social" style="left:183px;top:11px"></div>
    <div class="abs mini-social" style="left:196px;top:11px"></div>
    <div class="abs mini-social" style="left:209px;top:11px"></div>
    <div class="abs topbar" style="left:616px;top:9px">MY ACCOUNT</div>
    <svg class="abs" style="left:681px;top:9px" width="11" height="10" viewBox="0 0 11 10"><path d="M1 3h9l-1.2 5.5H2.2z" fill="#fff"/><circle cx="9" cy="2" r="2.6" fill="#e2c572"/></svg>
    <div class="abs topbar" style="left:696px;top:9px">$0.00</div>
    <div class="abs topbar-rule"></div>
    <div class="abs logo">LUMERA</div>
    <nav class="nav">
      <a style="left:405px">Home</a>
      <a style="left:444px">Treatment</a>
      <a style="left:507px">Portfolio</a>
      <a class="active" style="left:567px">Team</a>
      <a style="left:603px">Contact Us</a>
      <a style="left:668px">Booking</a>
    </nav>
  </header>

  <main>
    <h1 class="abs section-title">TEAM</h1>
    <div class="abs section-title-rule"></div>

    <article class="team-card" style="left:35px;top:225px">
      <div class="team-photo" role="img" aria-label="Portrait photograph of team member Maren Holt" style="background:linear-gradient(90deg,#2a2826 0%,#3c3a36 50%,#5a5447 100%)"></div>
      <div class="team-name">MAREN HOLT</div>
      <div class="learn-more">LEARN MORE</div>
    </article>
    <article class="team-card" style="left:381px;top:225px">
      <div class="team-photo" role="img" aria-label="Portrait photograph of team member Elias Brandt" style="background:linear-gradient(90deg,#c7c2ba 0%,#bfb9b0 50%,#d2cdc5 100%)"></div>
      <div class="team-name">ELIAS BRANDT</div>
      <div class="learn-more">LEARN MORE</div>
    </article>
    <article class="team-card" style="left:35px;top:496px">
      <div class="team-photo" role="img" aria-label="Portrait photograph of team member Ingrid Solli" style="background:linear-gradient(90deg,#e2e5e6 0%,#d9dbdb 55%,#cfd2d2 100%)"></div>
      <div class="team-name">INGRID SOLLI</div>
      <div class="learn-more">LEARN MORE</div>
    </article>
    <article class="team-card" style="left:381px;top:496px">
      <div class="team-photo" role="img" aria-label="Portrait photograph of team member Tora Lind" style="background:linear-gradient(90deg,#c8b89c 0%,#d6c6aa 50%,#b9aa92 100%)"></div>
      <div class="team-name">TORA LIND</div>
      <div class="learn-more">LEARN MORE</div>
    </article>

    <div class="to-top" style="left:714px;top:739px"><svg width="12" height="12" viewBox="0 0 12 12"><path d="M6 11V2M2 6l4-4 4 4" stroke="#fff" stroke-width="2" fill="none"/></svg></div>

    <div class="abs cta-rule"></div>
    <section class="abs cta">
      <p class="abs cta-text">It’s really easy to make an appointment!</p>
      <div class="abs cta-btn">MAKE AN APPOINTMENT</div>
    </section>
  </main>

  <footer>
    <div class="widget-title" style="left:34px">OPENING HOURS</div>
    <div class="widget-title" style="left:209px">LATEST ARTICLES</div>
    <div class="widget-title" style="left:384px">COVID-19 UPDATE</div>
    <div class="widget-title" style="left:558px">NEWSLETTER</div>

    <p class="abs body-copy" style="left:34px;top:920px;width:160px">Lorem ipsum dolor sit amet, consectetur adipiscing elit. Praesent ultricies dapibus mauris nec finibus.</p>
    <div class="hours-row" style="top:972px"><b>Mon-Fri</b>09:00 - 17:00</div>
    <div class="hours-row" style="top:998px"><b>Sat</b>10:00 - 14:00</div>
    <div class="hours-row" style="top:1024px"><b>Sun</b>Closed</div>

    <div class="article" style="top:919px"><h3>Velmora Wish List</h3><time>December 14, 2021</time></div>
    <div class="article-rule" style="top:952px"></div>
    <div class="article" style="top:960px"><h3>Basic Contouring Technique with Mascara</h3><time>December 14, 2021</time></div>
    <div class="article-rule" style="top:1006px"></div>
    <div class="article" style="top:1014px"><h3>New Services</h3><time>December 14, 2021</time></div>

    <p class="abs body-copy" style="left:384px;top:920px;width:160px">Etiam at risus et justo dignissim congue. Donec congue lacinia dui, a porttitor lectus condimentum laoreet.</p>
    <div class="widget-title" style="left:384px;top:979px">FIND US ONLINE</div>
    <div class="social-box" style="left:384px"><span></span></div>
    <div class="social-box" style="left:410px"><span></span></div>
    <div class="social-box" style="left:436px"><span></span></div>
    <div class="social-box" style="left:462px"><span></span></div>

    <div class="abs email-field">E-mail</div>
    <div class="abs subscribe">SUBSCRIBE</div>

    <div class="abs bottom-rule"></div>
    <p class="abs copyright">Copyright © 2021 All Right Reserved</p>
    <div class="to-top" style="left:714px;top:1135px;height:29px"><svg width="12" height="12" viewBox="0 0 12 12"><path d="M6 11V2M2 6l4-4 4 4" stroke="#fff" stroke-width="2" fill="none"/></svg></div>
  </footer>
</div>
</body>
</html>
```